RUXO9 biz card & Stationery

UXO9 is a personalized shopping experience brought to you, that lets you find and discover fashion goods through a collection of boutiques curated by taste-makers - celebrities, stylists, designers, and fashion bloggers. Boutiques uses visual technology to help fashionistas discover and shop their look and creates the opportunity for designers to showcase their collections and latest inspirations online.

RUXO9 is built on technology developed by our team of fashion experts who work with engineers to “teach” our computer systems to understand various patterns, pairings, and genre definitions. When signed into your account, RUXO9 learns about your style and preferences and in turn, provides you better results and recommendations over time. Ultimately, RUXO9 will provide shoppers with a much richer and interactive shopping experience and help drive traffic to retailers' websites.

We need a definitely cool business card. The card must be black! And must use our official logo which can be download from RUXO9.com

The address for Letter head and evenlop, please use 4821 Larkmoor Avenue, Sutie 520 Los Angeles CA90012, email will be anyone@RUXO9.com, website is www.RUXO9.com

thanks

We received some of the design, thanks. But most of the design are not what we want. We need a very clean version with black ground, you may also use some dark gray to add the element. please take a look at http://bleckvorn.no/work/#tarvik__olmstrup/, we do like this kind of design very much. hope it help.

```html
<!DOCTYPE html>
<html lang="en">
<head>
<meta charset="utf-8">
<title>RUXO9 Stationery</title>
<link rel="stylesheet" href="https://fonts.googleapis.com/css2?family=Questrial&display=swap">
<style>
  :root {
    --backdrop: #e2ddd8;
    --paper: #ffffff;
    --ink: #4a4a4a;
    --ink-soft: #6a6a6a;
    --black: #232323;
    --card-black: #272727;
    --disc-light: #f0f0f0;
    --disc-dark: #2d2d2d;
    --bar-gray: #4a4a4a;
    --light-text: #d8d8d8;
    --fold-line: #5a5a5a;
  }
  * { margin: 0; padding: 0; box-sizing: border-box; }
  html, body { width: 1200px; height: 900px; overflow: hidden; }
  body {
    background: var(--backdrop);
    font-family: "Questrial", "Century Gothic", sans-serif;
    position: relative;
  }
  .piece { position: absolute; overflow: hidden; }

  .wordmark { font-weight: 400; line-height: 1; letter-spacing: 0.01em; white-space: nowrap; }
  .backdrop-disc { position: absolute; border-radius: 50%; pointer-events: none; }
  .url-bar {
    position: absolute; left: 0; right: 0; bottom: 0;
    display: flex; align-items: center; justify-content: flex-end;
    letter-spacing: 0.18em;
  }
  .contact-list { list-style: none; }
  .contact-list li { display: flex; align-items: center; gap: 3px; white-space: nowrap; }
  .contact-list svg { flex: none; }
  address { font-style: normal; }

  /* Letterhead */
  .letterhead { left: 55px; top: 104px; width: 496px; height: 700px; background: var(--paper); }
  .letterhead .brand { position: absolute; left: 20px; top: 16px; color: var(--ink); }
  .letterhead .wordmark { font-size: 34px; }
  .letterhead .contact {
    position: absolute; left: 354px; top: 12px;
    font-size: 7.4px; color: var(--ink-soft); line-height: 1.35;
  }
  .letterhead .contact-list { margin-top: 3px; }
  .letterhead .backdrop-disc { width: 380px; height: 380px; right: -40px; bottom: 40px; background: var(--disc-light); }
  .letterhead .url-bar { height: 10px; background: var(--black); color: #fff; font-size: 8px; padding-right: 6px; }

  /* Business cards */
  .card { top: 128px; width: 210px; height: 120px; background: var(--card-black); color: var(--light-text); }
  .card-front { left: 648px; }
  .card-back { left: 876px; }
  .card .backdrop-disc { width: 120px; height: 120px; right: -20px; top: -10px; background: var(--disc-dark); }
  .card-front .holder { position: absolute; left: 10px; top: 30px; }
  .card-front .name { font-size: 9px; margin-bottom: 6px; }
  .card-front .details { font-size: 4.6px; line-height: 1.35; }
  .card-front .contact-list { margin-top: 3px; }
  .card-front .brand { position: absolute; left: 124px; top: 50px; }
  .card-front .wordmark { font-size: 20px; }
  .card-front .edge-band { position: absolute; left: 0; right: 0; bottom: 0; height: 8px; background: var(--bar-gray); }
  .card-back .brand { position: absolute; left: 0; right: 0; top: 42px; text-align: center; }
  .card-back .wordmark { font-size: 34px; }
  .card-back .url { position: absolute; left: 0; right: 0; bottom: 4px; text-align: center; font-size: 5px; letter-spacing: 0.18em; }

  /* Envelope front */
  .envelope-front { left: 581px; top: 272px; width: 570px; height: 247px; background: var(--card-black); color: var(--light-text); }
  .envelope-front .brand { position: absolute; left: 18px; top: 14px; }
  .envelope-front .wordmark { font-size: 40px; }
  .envelope-front .address { font-size: 6.4px; margin-top: 10px; white-space: nowrap; }
  .envelope-front .backdrop-disc { width: 260px; height: 260px; right: -50px; top: -10px; background: var(--disc-dark); }
  .envelope-front .url-bar { height: 16px; background: #3e3e3e; color: #eee; font-size: 8px; padding-right: 6px; }

  /* Envelope back */
  .envelope-back { left: 581px; top: 538px; width: 570px; height: 246px; background: #222222; }
  .envelope-back svg { display: block; }
</style>
</head>
<body>

<section class="piece letterhead" aria-label="Letterhead">
  <div class="backdrop-disc" aria-hidden="true"></div>
  <header class="brand">
    <div class="wordmark">RUXO9</div>
  </header>
  <address class="contact">
    <div>4821 Larkmoor Ave,</div>
    <div>Sutie 520 Los Angeles CA90012</div>
    <ul class="contact-list">
      <li><svg width="7" height="6" viewBox="0 0 7 6"><path d="M0 2 Q3.5 -0.5 7 2 L6 3 L4.8 2 L2.2 2 L1 3 Z M1.5 3 H5.5 L6.2 6 H0.8 Z" fill="#444"/></svg>: 1300 582 917</li>
      <li><svg width="7" height="7" viewBox="0 0 7 7"><rect x="1.5" y="0" width="4" height="7" rx="0.6" fill="#444"/><rect x="2.2" y="1" width="2.6" height="3" fill="#fff"/></svg>: 40078352196</li>
      <li><svg width="7" height="6" viewBox="0 0 7 6"><rect x="0.4" y="0.8" width="6.2" height="4.4" fill="none" stroke="#444" stroke-width="0.8"/><path d="M0.4 0.8 L3.5 3.4 L6.6 0.8" fill="none" stroke="#444" stroke-width="0.8"/></svg>: marisa@RUXO9.com</li>
    </ul>
  </address>
  <footer class="url-bar">www.RUXO9.com</footer>
</section>

<section class="piece card card-front" aria-label="Business card front">
  <div class="backdrop-disc" aria-hidden="true"></div>
  <div class="holder">
    <div class="name">Marisa Coleno</div>
    <div class="details">
      <div>4821 Larkmoor Ave,</div>
      <div>Sutie 520 Los Angeles CA90012</div>
      <div>W : www.RUXO9.com</div>
      <ul class="contact-list">
        <li><svg width="5" height="4" viewBox="0 0 7 6"><path d="M0 2 Q3.5 -0.5 7 2 L6 3 L4.8 2 L2.2 2 L1 3 Z M1.5 3 H5.5 L6.2 6 H0.8 Z" fill="#ddd"/></svg>: 1300 582 917</li>
        <li><svg width="5" height="5" viewBox="0 0 7 7"><rect x="1.5" y="0" width="4" height="7" rx="0.6" fill="#ddd"/></svg>: 40078352196</li>
        <li><svg width="5" height="4" viewBox="0 0 7 6"><rect x="0.4" y="0.8" width="6.2" height="4.4" fill="none" stroke="#ddd" stroke-width="0.9"/><path d="M0.4 0.8 L3.5 3.4 L6.6 0.8" fill="none" stroke="#ddd" stroke-width="0.9"/></svg>: marisa@RUXO9.com</li>
      </ul>
    </div>
  </div>
  <div class="brand">
    <div class="wordmark">RUXO9</div>
  </div>
  <div class="edge-band"></div>
</section>

<section class="piece card card-back" aria-label="Business card back">
  <div class="backdrop-disc" aria-hidden="true"></div>
  <div class="brand">
    <div class="wordmark">RUXO9</div>
  </div>
  <div class="url">www.RUXO9.com</div>
</section>

<section class="piece envelope-front" aria-label="Envelope front">
  <div class="backdrop-disc" aria-hidden="true"></div>
  <div class="brand">
    <div class="wordmark">RUXO9</div>
    <address class="address">4821 Larkmoor Ave, Sutie 520 LA CA90012</address>
  </div>
  <footer class="url-bar">www.RUXO9.com</footer>
</section>

<section class="piece envelope-back" aria-label="Envelope back">
  <svg width="570" height="246" viewBox="0 0 570 246">
    <path d="M2 2 C10 40 18 64 40 70 L270 104 Q285 107 300 104 L530 70 C552 64 560 40 568 2"
          fill="none" stroke="var(--fold-line)" stroke-width="0.8"/>
    <path d="M152 86 L12 236 Q6 242 2 244" fill="none" stroke="var(--fold-line)" stroke-width="0.8"/>
    <path d="M418 86 L558 236 Q564 242 568 244" fill="none" stroke="var(--fold-line)" stroke-width="0.8"/>
  </svg>
</section>

</body>
</html>
```